Brindle Offers is an online marketing platform.

A daily deals site for consumers a way to bring in new clients for clients and this is who the business cards are for. Industries - Food and Drink, Things To Do, Beauty and Spas, Staycations and Services.
Logo on one side.
Name - Owen Radley
Job Title - Sales Director
Phone Number - 07912358046
Email - owen@brindleoffers.co.uk
need same for second person
Name - Fiona Bracken
Job Title - Operations Director
Phone Number - 01632840275
Email - fiona@brindleoffers.co.uk
Bottom Right - Chatterbook Icon, Snapa Icon, Pipline Icon
Target Market(s)
Business owners of the above industries
Contact Information for Business Card
Name - Owen Radley
Name - Fiona Bracken
Look and feel

```html
<!DOCTYPE html>
<html lang="en">
<head>
<meta charset="utf-8">
<title>Brindle Offers – Business Cards</title>
<link rel="stylesheet" href="https://fonts.googleapis.com/css2?family=Lato:wght@400;700&display=swap">
<style>
  :root {
    --backdrop: #444444;
    --card-white: #ffffff;
    --brand-blue: #0455a4;
    --text-grey: #4a4a4a;
    --tagline-grey: #555555;
    --social-blue: #2f6db5;
    --social-sky: #1da1f2;
    --social-steel: #3f729b;
  }
  * { margin: 0; padding: 0; box-sizing: border-box; }
  html, body {
    width: 1200px; height: 900px; overflow: hidden;
    background: var(--backdrop);
    font-family: "Lato", Arial, sans-serif;
  }
  .canvas { position: relative; width: 1200px; height: 900px; }

  .card {
    position: absolute; top: 200px;
    width: 310px; height: 502px;
    box-shadow: 3px 4px 6px rgba(0,0,0,0.45);
  }
  .card--front {
    left: 253px; background: var(--card-white);
    border-radius: 62px 0 62px 0;
  }
  .card--back {
    left: 627px; background: var(--brand-blue);
    border-radius: 0 62px 0 62px;
  }

  /* Front: brand lockup */
  .brand {
    position: absolute; left: 44px; top: 132px;
    display: flex; align-items: center; gap: 8px;
  }
  .brand__dot {
    width: 34px; height: 34px; border-radius: 50%;
    background: var(--brand-blue); flex: none;
  }
  .brand__name {
    color: var(--brand-blue); font-weight: 700;
    font-size: 25px; letter-spacing: 0.5px; white-space: nowrap;
    text-transform: uppercase;
  }
  .brand__tagline {
    position: absolute; left: 86px; top: 179px;
    color: var(--tagline-grey); font-size: 14px;
    letter-spacing: 2px; text-transform: uppercase;
  }

  /* Front: contact block */
  .contact { position: absolute; left: 33px; top: 329px; }
  .contact__name {
    color: var(--brand-blue); font-weight: 700;
    font-size: 18px; letter-spacing: 0.3px;
  }
  .contact__role { color: var(--text-grey); font-size: 14px; margin-top: 1px; }
  .contact__list { list-style: none; margin-top: 13px; }
  .contact__item {
    display: flex; align-items: center; gap: 5px;
    color: var(--text-grey); font-size: 14.5px; line-height: 18.5px;
  }
  .contact__icon { width: 12px; height: 12px; flex: none; }

  .social { display: flex; gap: 2px; margin-top: 14px; }
  .social__badge { width: 17px; height: 17px; border-radius: 50%; }
  .social__badge--chatterbook { background: var(--social-blue); }
  .social__badge--pipline { background: var(--social-sky); }
  .social__badge--snapa { background: var(--social-steel); }

  /* Back */
  .back-mark {
    position: absolute; left: 0; right: 0; top: 162px;
    display: flex; flex-direction: column; align-items: center; gap: 18px;
  }
  .back-mark__dot {
    width: 104px; height: 104px; border-radius: 50%;
    background: var(--card-white);
  }
  .back-mark__name {
    color: var(--card-white); font-weight: 700;
    font-size: 26px; letter-spacing: 0.5px; text-transform: uppercase;
  }
  .back-url {
    position: absolute; left: 0; right: 0; top: 440px;
    text-align: center; color: var(--card-white); font-size: 14px;
  }
</style>
</head>
<body>
<main class="canvas">

  <section class="card card--front" aria-label="Business card front">
    <div class="brand">
      <span class="brand__dot"></span>
      <span class="brand__name">Brindle Offers</span>
    </div>
    <p class="brand__tagline">Save. See. Relax.</p>

    <div class="contact">
      <h1 class="contact__name">OWEN RADLEY</h1>
      <p class="contact__role">Sales Director</p>
      <ul class="contact__list">
        <li class="contact__item">
          <svg class="contact__icon" viewBox="0 0 12 12" aria-hidden="true">
            <path fill="#0455a4" d="M1 4c0-2 2-3 5-3s5 1 5 3v1H8.5V3.8c-1.5-.6-3.5-.6-5 0V5H1zM3 6h6l1.5 4.5h-9z"/>
            <circle cx="6" cy="8" r="1.3" fill="#fff"/>
          </svg>
          07912358046
        </li>
        <li class="contact__item">
          <svg class="contact__icon" viewBox="0 0 12 12" aria-hidden="true">
            <rect x="1" y="2.5" width="10" height="7" fill="#0455a4"/>
            <path d="M1.5 3l4.5 3.5L10.5 3" fill="none" stroke="#fff" stroke-width="0.9"/>
          </svg>
          owen@brindleoffers.co.uk
        </li>
        <li class="contact__item">
          <svg class="contact__icon" viewBox="0 0 12 12" aria-hidden="true">
            <circle cx="6" cy="6" r="5" fill="#0455a4"/>
            <path d="M3.5 4c1 0 1.5 1 2.5 1s.5 1.5-.5 2S4 8.5 4.5 9.5M7.5 3c.5.5 1.5.5 2 1.5" fill="none" stroke="#fff" stroke-width="0.9"/>
          </svg>
          www.brindleoffers.co.uk
        </li>
      </ul>
      <div class="social" aria-label="Chatterbook, Pipline and Snapa">
        <span class="social__badge social__badge--chatterbook"></span>
        <span class="social__badge social__badge--pipline"></span>
        <span class="social__badge social__badge--snapa"></span>
      </div>
    </div>
  </section>

  <section class="card card--back" aria-label="Business card back">
    <div class="back-mark">
      <span class="back-mark__dot"></span>
      <span class="back-mark__name">Brindle Offers</span>
    </div>
    <p class="back-url">www.brindleoffers.co.uk</p>
  </section>

</main>
</body>
</html>
```